Pet store web design

I would like to redesign my current online store (http://brindlecove.example)
I'm looking for a clean, modern design. Any ideas are welcome..

Industry/Entity Type

Pet

Number of Pages Required

3 page

```html
<!DOCTYPE html>
<html lang="en">
<head>
<meta charset="utf-8">
<title>Brindle Cove — Pet Store</title>
<link href="https://fonts.googleapis.com/css2?family=Open+Sans:wght@300;400;600;700;800&display=swap" rel="stylesheet">
<style>
:root{
  --orange:#f4a21b;
  --orange-dark:#e08a0c;
  --teal:#1ba3a6;
  --green:#8cc63f;
  --ink:#333;
  --muted:#888;
  --line:#e2e2e2;
  --panel:#f4f4f4;
  --footer:#0e0e0e;
  --white:#fff;
}
*{box-sizing:border-box;margin:0;padding:0}
html,body{width:1200px;height:2396px;overflow:hidden}
body{font-family:"Open Sans",Arial,sans-serif;color:var(--ink);background:var(--white);position:relative;font-size:13px}
.abs{position:absolute}

/* header */
.header{left:0;top:0;width:1200px;height:200px;background:linear-gradient(#f7f7f7,#ececec)}
.brand{left:120px;top:14px;display:flex;align-items:center;gap:10px}
.brand-dot{width:34px;height:34px;border-radius:50%;background:var(--orange)}
.brand-name{font-size:30px;font-weight:800;color:var(--orange)}
.follow{left:350px;top:66px;display:flex;align-items:center;gap:6px;font-size:12px;color:var(--muted)}
.follow i{display:block;width:20px;height:20px;border-radius:50%;background:#9a9a9a}
.follow .help{margin-left:10px}
.search{left:600px;top:22px;width:230px;height:28px;border:1px solid #ccc;background:#fff;border-radius:3px}
.search svg{position:absolute;right:8px;top:6px}
.cart{left:845px;top:20px;font-size:11px;color:var(--muted)}
.cart b{display:block;margin-top:6px;background:var(--orange);color:#fff;font-weight:600;padding:3px 12px;border-radius:3px;width:max-content}
.account{left:960px;top:20px;font-size:11px;color:var(--muted);line-height:22px}
.account span{display:block;border:1px solid #ccc;background:#fff;border-radius:3px;padding:0 12px;margin-bottom:4px;width:110px}

.nav{left:120px;top:150px;width:960px;height:36px;display:flex;align-items:center;gap:6px;border-bottom:3px solid var(--orange)}
.nav a{display:block;text-decoration:none;color:var(--ink);font-size:13px;font-weight:600;padding:8px 20px;background:#fff;border:1px solid #ddd;border-bottom:none;border-radius:3px 3px 0 0}
.nav a.active{background:var(--orange);color:#fff;border-color:var(--orange)}

/* hero */
.promo-line{left:0;top:206px;width:1200px;text-align:center;font-size:30px;font-weight:300;letter-spacing:3px;color:#444}
.hero{left:120px;top:250px;width:960px;height:450px;background:linear-gradient(180deg,#e6ecef 0%,#cfd9c2 45%,#7fb63b 75%,#5e9a28 100%);border-radius:3px}
.hero-arrow{top:458px;width:34px;height:34px;border-radius:50%;background:#fff;box-shadow:0 1px 4px rgba(0,0,0,.3)}
.hero-arrow svg{margin:9px}
.hero-arrow.left{left:103px}.hero-arrow.right{left:1063px}
.hero-shadow{left:120px;top:708px;width:960px;height:8px;border-radius:50%;background:radial-gradient(ellipse at center,rgba(0,0,0,.18),transparent 70%)}

/* featured */
.section-title{left:120px;top:752px;width:960px;text-align:center}
.section-title::before{content:"";position:absolute;left:0;right:0;top:50%;border-top:1px solid var(--line)}
.section-title h2{position:relative;display:inline-block;background:#fff;padding:0 16px;font-size:28px;font-weight:300;color:#555}
.tabs{left:120px;top:826px;width:200px}
.tabs li{list-style:none;font-size:12px;padding:10px 14px;border:1px solid var(--line);border-top:none;color:#666}
.tabs li:first-child{border-top:1px solid var(--line);background:var(--teal);color:#fff;border-color:var(--teal)}
.pager{left:984px;top:792px;display:flex;gap:4px;align-items:center;font-size:11px;color:var(--muted)}
.pager b{display:block;width:20px;height:20px;border:1px solid #ccc;background:#fff}
.pager b.on{background:var(--teal);border-color:var(--teal)}

.card{width:180px;height:270px;border:1px solid var(--line);background:#fff;text-align:center}
.card.tall{height:290px}
.card.hl{border:2px solid var(--orange)}
.card .name{font-size:11px;color:var(--muted);margin:10px 8px 4px;text-align:left;white-space:nowrap}
.card .price-top{font-size:11px;color:var(--muted);text-align:left;margin:0 8px}
.card .pic{height:130px;margin:8px 10px;border-radius:2px}
.card .price{font-size:22px;color:#444;font-weight:400;margin-top:6px}
.card .price-panel{position:absolute;left:0;right:0;bottom:0;height:56px;background:var(--panel)}
.card .price-panel .price{margin-top:14px}
.sale{position:absolute;right:10px;top:10px;width:40px;height:40px;border-radius:50%;background:var(--teal);color:#fff;font-size:11px;font-weight:600;line-height:40px}
.stars{display:flex;gap:3px;margin:0 8px}
.stars svg{display:block}
.addcart{display:inline-block;margin-top:14px;font-size:10px;padding:4px 12px;border:1px solid #ccc;background:#f3f3f3;color:#555;border-radius:2px}

.row-line{left:120px;width:960px;border-top:3px solid #ddd}

/* promos */
.promo{top:1560px;height:230px;border-radius:2px;overflow:hidden}
.promo .pic{position:absolute;inset:0}
.promo .tag{position:absolute;left:12px;top:14px;font-size:26px;font-weight:800;color:#fff}
.testimonial{left:784px;top:1560px;width:296px;height:230px;background:var(--green);color:#fff;padding:18px 18px}
.testimonial h3{font-size:24px;font-weight:600;margin-bottom:12px}
.testimonial p{font-size:12px;line-height:18px}
.testimonial .who{margin-top:12px;font-size:12px}

.newsletter{left:120px;top:1808px;width:960px;height:46px;background:var(--orange);color:#fff;display:flex;align-items:center;padding:0 16px;font-size:14px}
.newsletter .field{margin-left:auto;width:220px;height:28px;background:#fff;color:var(--muted);font-size:12px;line-height:28px;padding-left:10px;border-radius:2px 0 0 2px}
.newsletter .go{width:30px;height:28px;background:var(--teal);border-radius:0 2px 2px 0}

.features{left:120px;top:1890px;width:960px;height:110px;display:flex;justify-content:space-around;border-bottom:1px solid var(--line)}
.feature{display:flex;gap:12px;align-items:flex-start;width:200px}
.feature .ico{width:48px;height:48px;border-radius:50%;background:var(--orange);flex:none;display:flex;align-items:center;justify-content:center}
.feature h4{font-size:13px;color:var(--orange);font-weight:700}
.feature p{font-size:10px;color:var(--muted);line-height:14px}

/* footer */
.footer{left:0;top:2110px;width:1200px;height:286px;background:var(--footer);color:#ccc}
.fcols{position:absolute;left:120px;top:36px;width:960px;display:flex;gap:30px}
.fcol{width:160px}
.fcol h5{color:#fff;font-size:12px;font-weight:700;margin-bottom:12px}
.fcol li{list-style:none;font-size:11px;line-height:20px;color:#aaa}
.safe{width:200px;margin-left:auto}
.badge{width:120px;height:30px;background:#fff;border-radius:2px;margin-bottom:18px}
.cards{display:flex;gap:8px}
.cards i{display:block;width:44px;height:28px;background:#fff;border-radius:3px}
.copy{position:absolute;left:0;right:0;bottom:22px;text-align:center;font-size:11px;color:#888}
</style>
</head>
<body>

<header class="header abs">
  <div class="brand abs"><span class="brand-dot"></span><span class="brand-name">Brindle Cove</span></div>
  <div class="follow abs">Follow us: <i></i><i></i><i></i><i></i><i></i><span class="help">| Help</span></div>
  <div class="search abs"><svg width="14" height="14" viewBox="0 0 14 14"><circle cx="6" cy="6" r="4.5" fill="none" stroke="#999" stroke-width="1.6"/><line x1="9.5" y1="9.5" x2="13" y2="13" stroke="#999" stroke-width="1.6"/></svg></div>
  <div class="cart abs">Items in cart: 0<b>Checkout</b></div>
  <div class="account abs"><span>Join Now</span><span>Log In</span></div>
  <nav class="nav abs">
    <a class="active">HOME</a><a>DOG</a><a>CAT</a><a>FISH</a><a>BIRD</a><a>SMALL PET</a><a>GIFTS</a><a>SHOP BY BRAND</a>
  </nav>
</header>

<div class="promo-line abs">FREE DELIVERY ON ORDERS OVER $79</div>
<div class="hero abs" role="img" aria-label="Photo of a girl walking with a golden retriever on a sunny lawn"></div>
<div class="hero-arrow left abs"><svg width="16" height="16" viewBox="0 0 16 16"><path d="M10 3 5 8l5 5" fill="none" stroke="#666" stroke-width="2"/></svg></div>
<div class="hero-arrow right abs"><svg width="16" height="16" viewBox="0 0 16 16"><path d="M6 3l5 5-5 5" fill="none" stroke="#666" stroke-width="2"/></svg></div>
<div class="hero-shadow abs"></div>

<div class="section-title abs"><h2>Featured Products</h2></div>
<div class="pager abs">1 of 5 <b></b><b class="on"></b></div>
<ul class="tabs abs">
  <li>Soft Rubber Toys</li><li>Small pet supplies</li><li>Cat Dishes</li><li>All New Products</li>
</ul>

<div class="card hl abs" style="left:345px;top:812px">
  <div class="sale">Sale</div>
  <div class="name">Nest Bed - Large Fawn</div>
  <div class="price-top">$180.00</div>
  <div class="pic" role="img" aria-label="Product photo of a round plush dog bed" style="background:linear-gradient(#e9e4d8,#b9a98c)"></div>
  <div class="price-panel"><div class="price">$162.32</div></div>
</div>
<div class="card abs" style="left:550px;top:812px">
  <div class="name">Orthopaedic Dog Bed</div>
  <div class="stars">
    <svg width="14" height="14" viewBox="0 0 10 10"><path d="M5 0l1.5 3.3 3.5.3-2.7 2.3.9 3.5L5 7.5 1.8 9.4l.9-3.5L0 3.6l3.5-.3z" fill="#f4a21b"/></svg>
    <svg width="14" height="14" viewBox="0 0 10 10"><path d="M5 0l1.5 3.3 3.5.3-2.7 2.3.9 3.5L5 7.5 1.8 9.4l.9-3.5L0 3.6l3.5-.3z" fill="#f4a21b"/></svg>
    <svg width="14" height="14" viewBox="0 0 10 10"><path d="M5 0l1.5 3.3 3.5.3-2.7 2.3.9 3.5L5 7.5 1.8 9.4l.9-3.5L0 3.6l3.5-.3z" fill="#f4a21b"/></svg>
    <svg width="14" height="14" viewBox="0 0 10 10"><path d="M5 0l1.5 3.3 3.5.3-2.7 2.3.9 3.5L5 7.5 1.8 9.4l.9-3.5L0 3.6l3.5-.3z" fill="#f4a21b"/></svg>
    <svg width="14" height="14" viewBox="0 0 10 10"><path d="M5 0l1.5 3.3 3.5.3-2.7 2.3.9 3.5L5 7.5 1.8 9.4l.9-3.5L0 3.6l3.5-.3z" fill="#ccc"/></svg>
  </div>
  <div class="price-top">Grey Fleece - Small/Medium</div>
  <div class="pic" role="img" aria-label="Product photo of a grey orthopaedic dog bed" style="background:linear-gradient(#eee,#a9a9a9);height:112px"></div>
  <div class="price-panel"><div class="price">$86.84</div></div>
</div>
<div class="card abs" style="left:755px;top:812px">
  <div class="name">Treat Jar Set - Mixed</div>
  <div class="price-top">$220.00</div>
  <div class="pic" role="img" aria-label="Product photo of a row of pet food storage bins" style="background:linear-gradient(90deg,#7a5a3a,#b08a5a,#5c5c5c,#8a6a4a)"></div>
  <div class="price-panel"><div class="price">$190.00</div></div>
</div>
<div class="row-line abs" style="top:1130px"></div>

<div class="card tall abs" style="left:120px;top:1170px">
  <div class="name">Shell Dog Costume - Large</div><div class="price-top">$32.00</div>
  <div class="pic" role="img" aria-label="Product photo of a dog wearing a striped costume" style="background:linear-gradient(#f6f6f6,#d8dbe4)"></div>
  <span class="addcart">ADD TO CART</span>
</div>
<div class="card tall abs" style="left:315px;top:1170px">
  <div class="name">Shell Dog Costume - Large</div><div class="price-top">$32.00</div>
  <div class="pic" role="img" aria-label="Product photo of a small dog in a green costume" style="background:linear-gradient(#f6f6f6,#cfe3a8)"></div>
  <span class="addcart">ADD TO CART</span>
</div>
<div class="card tall abs" style="left:510px;top:1170px">
  <div class="name">Potty Grass Mat - Small</div><div class="price-top">$32.00</div>
  <div class="pic" role="img" aria-label="Product photo of a grass potty mat for dogs" style="background:linear-gradient(#f6f6f6,#6f8f4a)"></div>
  <span class="addcart">ADD TO CART</span>
</div>
<div class="card tall abs" style="left:705px;top:1170px">
  <div class="name">Dog Paw Cleaning Kit</div><div class="price-top">$19.00</div>
  <div class="pic" role="img" aria-label="Product photo of a dog grooming kit" style="background:linear-gradient(#f6f6f6,#d9d9d9)"></div>
  <span class="addcart">ADD TO CART</span>
</div>
<div class="card tall abs" style="left:900px;top:1170px">
  <div class="name">Dog Pet Treadmill</div><div class="price-top">$849.00</div>
  <div class="pic" role="img" aria-label="Product photo of a red dog treadmill" style="background:linear-gradient(#f6f6f6,#c8463a)"></div>
  <span class="addcart">ADD TO CART</span>
</div>
<div class="row-line abs" style="top:1500px"></div>

<div class="promo abs" style="left:120px;width:316px">
  <div class="pic" role="img" aria-label="Photo of colourful soft rubber dog toys" style="background:linear-gradient(135deg,#f3c14a,#e46a3a 55%,#3a9ad9)"></div>
  <span class="tag">SOFT RUBBER TOYS</span>
</div>
<div class="promo abs" style="left:452px;width:316px">
  <div class="pic" role="img" aria-label="Photo of a small dog resting in a round bed" style="background:linear-gradient(135deg,#d9c4c8,#a98b90)"></div>
  <span class="tag">SMALL DOG BEDS</span>
</div>
<div class="testimonial abs">
  <h3>What Our Client Say!</h3>
  <p>We ordered a bed and treats for our two rescue dogs and both arrived fast, well packed and exactly as shown. Friendly help and fair prices every time.</p>
  <div class="who">Mara Linden · Dog Care</div>
</div>

<div class="newsletter abs">Keep up to date on the latest from Brindle Cove. We love pets.<span class="field">Enter Email Address</span><span class="go"></span></div>

<div class="features abs">
  <div class="feature"><span class="ico"><svg width="24" height="18" viewBox="0 0 24 18"><rect x="1" y="3" width="13" height="9" fill="#fff"/><path d="M14 6h5l3 3v3h-8z" fill="#fff"/><circle cx="6" cy="14" r="2.5" fill="#fff"/><circle cx="18" cy="14" r="2.5" fill="#fff"/></svg></span><div><h4>DELIVERY</h4><p>Free on orders over $79<br>View details &gt;</p></div></div>
  <div class="feature"><span class="ico"><svg width="22" height="22" viewBox="0 0 22 22"><path d="M4 11a7 7 0 1 0 2-5" fill="none" stroke="#fff" stroke-width="2.4"/><path d="M3 2v6h6" fill="none" stroke="#fff" stroke-width="2.4"/></svg></span><div><h4>RETURNS</h4><p>Easy thirty day returns<br>View details &gt;</p></div></div>
  <div class="feature"><span class="ico"><svg width="20" height="22" viewBox="0 0 20 22"><text x="10" y="18" text-anchor="middle" font-size="20" font-weight="700" fill="#fff" font-family="Open Sans,sans-serif">?</text></svg></span><div><h4>QUESTIONS?</h4><p>Read our pet care help<br>View details &gt;</p></div></div>
  <div class="feature"><span class="ico"><svg width="22" height="22" viewBox="0 0 22 22"><path d="M5 2l4 4-2 3c1.5 3 3 4.5 6 6l3-2 4 4-3 3C9 19 3 13 2 5z" fill="#fff"/></svg></span><div><h4>LET US HELP</h4><p>Call or chat with our team<br>View details &gt;</p></div></div>
</div>

<footer class="footer abs">
  <div class="fcols">
    <div class="fcol"><h5>SHOP NOW</h5><ul><li>Dog</li><li>Cat</li><li>Fish</li><li>Bird</li><li>Gifts</li><li>Our Deals</li></ul></div>
    <div class="fcol"><h5>SERVICES</h5><ul><li>Pet Grooming</li><li>Pet Adoption</li><li>Vet Visit Help</li><li>Pet Hotel</li></ul></div>
    <div class="fcol"><h5>SHOPPING ONLINE</h5><ul><li>Delivery Information</li><li>Privacy Policy</li><li>Returns Policy</li><li>Terms and Conditions</li></ul></div>
    <div class="fcol"><h5>ABOUT US</h5><ul><li>About Us</li><li>Careers</li><li>Blog</li></ul></div>
    <div class="fcol safe"><h5>SHOP IN SAFETY</h5><div class="badge"></div><h5>WE ACCEPT</h5><div class="cards"><i></i><i></i><i></i></div></div>
  </div>
  <div class="copy">Copyright 2014 Brindle Cove Store. All Rights Reserved.</div>
</footer>

</body>
</html>
```